Bourbon Label Design For a Unique Craft Distillery

We are a craft distillery located in Mount Holly Nj looking for a label design for our new bourbon brand. The Name of the bourbon is going to be called "Iron Meadow" and the type of bourbon is a "straight Bourbon Whiskey". The First file are the pictures of our current brands. Would like the design to look Vintage but pop. The Bourbon will be a top shelf item. The Pictures of the other bottle are brands we like.

Target Market(s)

21-65 years old

Font styles to use
Decorative
Script

Colors
ec1f27
3176b5
1b1b1b
f5f5f5

Requirements
Must have
• vintage look, and pop !

```html
<!DOCTYPE html>
<html lang="en">
<head>
<meta charset="UTF-8">
<title>Iron Meadow Straight Bourbon Whiskey Label</title>
<link rel="stylesheet" href="https://fonts.googleapis.com/css2?family=Alfa+Slab+One&family=Oswald:wght@500;600;700&display=swap">
<style>
  :root {
    --bg: #e6e9ee;
    --gold-light: #f1d27a;
    --gold: #d8ab3f;
    --gold-deep: #a9781f;
    --ink: #1b1b1b;
    --red: #ec1f27;
    --red-deep: #a8140f;
    --paper: #f5f5f5;
  }
  * { margin: 0; padding: 0; box-sizing: border-box; }
  html, body { width: 970px; height: 1200px; overflow: hidden; background: var(--bg); }
  .canvas { position: relative; width: 970px; height: 1200px; background: radial-gradient(ellipse at 50% 40%, #f3f5f8 0%, var(--bg) 70%); }
  .label { position: absolute; left: 155px; top: 140px; width: 660px; height: 920px; color: var(--ink); font-family: "Oswald", sans-serif; }
  .label-shape { position: absolute; inset: 0; }
  .label-text { position: absolute; left: 0; width: 100%; text-align: center; }
  .vintage { top: 58px; font-size: 58px; font-weight: 700; letter-spacing: 1px; line-height: 1; }
  .vintage .star { font-size: 34px; vertical-align: middle; margin: 0 14px; }
  .year-row { top: 142px; font-size: 28px; font-weight: 600; line-height: 1; }
  .batch, .batch-number { position: absolute; top: 142px; font-size: 26px; font-weight: 600; line-height: 1; }
  .batch { left: 44px; }
  .batch-number { right: 52px; }
  .brand-name { top: 208px; font-family: "Alfa Slab One", serif; font-size: 104px; line-height: 106px; letter-spacing: 2px; }
  .band-art { position: absolute; left: 62px; top: 478px; width: 360px; height: 86px; background: linear-gradient(100deg, var(--red-deep) 0%, #5a0c08 70%, var(--red-deep) 100%); transform: skewY(-4deg); opacity: 0.85; }
  .style-name { top: 602px; font-size: 40px; font-weight: 600; line-height: 1; transform: rotate(-2deg); }
  .volume { top: 675px; font-size: 26px; font-weight: 600; color: var(--gold-light); line-height: 1; word-spacing: 6px; }
  .aging { top: 748px; font-size: 19px; font-weight: 600; line-height: 1.35; }
</style>
</head>
<body>
<main class="canvas">
  <section class="label">
    <svg class="label-shape" viewBox="0 0 660 920" width="660" height="920" aria-hidden="true">
      <defs>
        <linearGradient id="goldFoil" x1="0" y1="0" x2="1" y2="1">
          <stop offset="0" stop-color="#a9781f"/>
          <stop offset="0.3" stop-color="#f1d27a"/>
          <stop offset="0.55" stop-color="#d8ab3f"/>
          <stop offset="0.8" stop-color="#f1d27a"/>
          <stop offset="1" stop-color="#a9781f"/>
        </linearGradient>
      </defs>
      <path d="M0,50 L90,50 Q112,50 130,30 L168,0 L492,0 L530,30 Q548,50 570,50 L660,50 L660,700 L560,770 L330,920 L100,770 L0,700 Z" fill="url(#goldFoil)" stroke="#1b1b1b" stroke-width="4"/>
      <path d="M18,68 L98,68 Q122,68 142,46 L176,18 L484,18 L518,46 Q538,68 562,68 L642,68 L642,690 L548,756 L330,898 L112,756 L18,690 Z" fill="none" stroke="#1b1b1b" stroke-width="7"/>
      <path d="M32,82 L104,82 Q130,82 150,60 L182,32 L478,32 L510,60 Q530,82 556,82 L628,82 L628,682 L540,744 L330,882 L120,744 L32,682 Z" fill="none" stroke="#1b1b1b" stroke-width="2"/>
      <line x1="32" y1="128" x2="628" y2="128" stroke="#1b1b1b" stroke-width="3"/>
      <line x1="32" y1="182" x2="628" y2="182" stroke="#1b1b1b" stroke-width="3"/>
      <line x1="118" y1="128" x2="118" y2="182" stroke="#1b1b1b" stroke-width="2"/>
      <line x1="542" y1="128" x2="542" y2="182" stroke="#1b1b1b" stroke-width="2"/>
      <polygon points="32,490 628,450 628,560 32,600" fill="#ec1f27"/>
      <line x1="32" y1="490" x2="628" y2="450" stroke="#1b1b1b" stroke-width="3"/>
      <line x1="32" y1="600" x2="628" y2="560" stroke="#1b1b1b" stroke-width="3"/>
      <polygon points="60,662 600,634 600,706 60,734" fill="#1b1b1b"/>
    </svg>
    <p class="label-text vintage"><span class="star">★</span>VINTAGE<span class="star">★</span></p>
    <p class="batch">BATCH</p>
    <p class="label-text year-row">IN THE YEAR OF 2016</p>
    <p class="batch-number">60</p>
    <h1 class="label-text brand-name">IRON<br>MEADOW</h1>
    <div class="band-art" role="img" aria-label="Engraved illustration of a streamliner locomotive pulling a passenger train past a telegraph pole"></div>
    <p class="label-text style-name">STRAIGHT BOURBON WHISKEY</p>
    <p class="label-text volume">ALC 16% VOL | 700 ML</p>
    <p class="label-text aging">AGED IN A BRAND NEW<br>CHARRED WHITE OAK BARREL</p>
  </section>
</main>
</body>
</html>
```